Refresh of Business Card Design

Want to refresh the business card design with the new logo while adhering to style guide as attached. Would like to match feel of website www.brimwickdrives.com

```html
<!DOCTYPE html>
<html lang="en">
<head>
<meta charset="utf-8">
<title>Brimwick Drives – Business Card</title>
<link rel="stylesheet" href="https://fonts.googleapis.com/css2?family=Source+Sans+3:wght@400;700&display=swap">
<style>
  :root {
    --bg: #8a8a8a;
    --red: #c8262e;
    --red-dark: #ad2430;
    --rule: #9a9a9a;
    --ink: #1a1a1a;
    --white: #ffffff;
    --black: #050505;
  }
  * { margin: 0; padding: 0; box-sizing: border-box; }
  html, body { width: 1093px; height: 1200px; overflow: hidden; }
  body {
    background: var(--bg);
    font-family: "Source Sans 3", sans-serif;
    color: var(--ink);
    position: relative;
  }
  .card {
    position: absolute;
    left: 264px;
    width: 580px;
    height: 356px;
    border-radius: 24px;
    overflow: hidden;
  }
  .card--front { top: 226px; background: var(--white); }
  .card--back { top: 621px; height: 360px; background: var(--black); }

  .band {
    position: absolute; left: 0; top: 0; width: 100%; height: 114px;
    background: linear-gradient(to bottom, var(--red), var(--red-dark));
    border-bottom: 3px solid var(--rule);
  }
  .brand {
    position: absolute; left: 0; width: 100%;
    display: flex; align-items: center; justify-content: center; gap: 12px;
    font-weight: 700; letter-spacing: 2px; text-transform: uppercase;
  }
  .brand__dot { border-radius: 50%; flex: none; }
  .card--front .brand { top: 38px; font-size: 28px; color: var(--white); }
  .card--front .brand__dot { width: 22px; height: 22px; background: var(--white); }
  .card--back .brand { top: 156px; font-size: 36px; color: var(--white); }
  .card--back .brand__dot { width: 30px; height: 30px; background: var(--red); }

  .person { position: absolute; right: calc(580px - 267px); top: 230px; text-align: right; }
  .person__name { font-size: 25px; font-weight: 700; color: var(--red); line-height: 1; letter-spacing: 0.2px; }
  .person__role { font-size: 17px; line-height: 1.1; margin-top: 3px; }

  .divider { position: absolute; left: 289px; top: 231px; width: 1px; height: 55px; background: var(--ink); }

  .contacts { position: absolute; left: 311px; top: 225px; list-style: none; }
  .contacts li { display: flex; align-items: center; gap: 8px; height: 21px; font-size: 17px; }
  .contacts svg { width: 16px; height: 16px; flex: none; }

  .address {
    position: absolute; left: 0; top: 304px; width: 100%;
    text-align: center; font-size: 17px;
  }
</style>
</head>
<body>
  <section class="card card--front" aria-label="Card front">
    <div class="band"></div>
    <div class="brand"><span class="brand__dot"></span>Brimwick Drives</div>

    <div class="person">
      <p class="person__name">DALE HORVATH</p>
      <p class="person__role">Sales</p>
    </div>
    <div class="divider"></div>

    <ul class="contacts">
      <li>
        <svg viewBox="0 0 16 16" aria-hidden="true"><path d="M3.5 1.5l2.5 2.8-1.3 1.6c.8 1.8 2.3 3.3 4 4.2l1.6-1.3 2.8 2.5-1.5 2.2C7 13.5 2.5 9 1.5 3z" fill="var(--red)"/><path d="M10 2a4 4 0 0 1 4 4M10 4.3A1.8 1.8 0 0 1 11.7 6" fill="none" stroke="var(--red)" stroke-width="1.2"/></svg>
        555.201.4830
      </li>
      <li>
        <svg viewBox="0 0 16 16" aria-hidden="true"><rect x="1" y="3" width="14" height="10" fill="var(--red)"/><path d="M1 3l7 6 7-6M1 13l5-5M15 13l-5-5" fill="none" stroke="var(--white)" stroke-width="1"/></svg>
        dhorvath@brimwickdrives.com
      </li>
      <li>
        <svg viewBox="0 0 16 16" aria-hidden="true"><g fill="none" stroke="var(--red)" stroke-width="1.2"><circle cx="8" cy="8" r="6.5"/><ellipse cx="8" cy="8" rx="3" ry="6.5"/><path d="M1.5 8h13M2.5 4.8h11M2.5 11.2h11"/></g></svg>
        www.brimwickdrives.com
      </li>
    </ul>

    <p class="address">P.O.Box 40215 Fairlow, TX 7934 | 218 Harlan Rd Kestrel, Texas 79462</p>
  </section>

  <section class="card card--back" aria-label="Card back">
    <div class="brand"><span class="brand__dot"></span>Brimwick Drives</div>
  </section>
</body>
</html>
```